Flyer für Tiertherapeutin
Eine sehr motivierte und kreative Designerin. Schon der erste Vorschlag war ganz nach meinen Vorstellungen.
Zielgruppe
Ich bin Tiertherapeutin für TCVM und Ernährungsberaterin für Hunde und Katzen. Mittels Akupunktur, Lasertherapie, Mykotherapie und Ernährungsberatung kommt es zu einer Linderung vorhandener Schmerzen, eine verbesserte Regulation der Organe und einer Steigerung das Wohlbefindens sowie Lebensqualität.
Zielgruppe sind überwiegend weibliche Hunde- und Katzenbesitzer mit erkrankten Tieren.
Aufgabenstellung
Flyer sollte klappbar sein. Logo und mein Name und Kontaktdaten sollten enthalten sein.

```html
<!DOCTYPE html>
<html lang="de">
<head>
<meta charset="utf-8">
<title>Flyer Tiertherapie – Pfotenruh</title>
<link href="https://fonts.googleapis.com/css2?family=Nunito:wght@400;600;700&display=swap" rel="stylesheet">
<style>
:root{
  --bg:#ececec;
  --paper:#ffffff;
  --panel-grey:#e4e4e4;
  --accent:#e2ab7f;
  --accent-deep:#c8976f;
  --accent-soft:#f0cfb3;
  --ink:#3a3a3a;
  --ink-soft:#5a5a5a;
  --on-accent:#ffffff;
}
*{box-sizing:border-box;margin:0;padding:0}
html,body{width:1200px;height:900px;overflow:hidden;background:var(--bg);font-family:'Nunito',sans-serif;color:var(--ink)}
.spread{position:absolute;top:190px;width:460px;height:520px;display:flex;box-shadow:0 18px 30px rgba(0,0,0,.12)}
.spread--outside{left:110px}
.spread--inside{left:630px}
.panel{position:relative;width:230px;height:520px;overflow:hidden}
.panel--white{background:var(--paper)}
.panel--grey{background:var(--panel-grey)}
.abs{position:absolute}
.photo{position:absolute}
.t-small{font-size:7.4px;line-height:1.45}
.strong{font-weight:700}

/* about */
.about-box{left:14px;top:70px;width:214px;height:300px;background:var(--accent);clip-path:polygon(0 8px,100% 0,100% 100%,0 100%);color:var(--on-accent)}
.portrait{left:57px;top:16px;width:122px;height:122px;border-radius:50%;background:radial-gradient(circle at 50% 40%,#d8c8b8,#8a8f9a);border:3px solid var(--paper)}
.about-title{left:14px;top:162px;font-size:11.5px;font-weight:600}
.about-text{left:14px;top:182px;width:180px}
.about-invite{left:14px;top:270px;width:180px}
.signature{left:14px;top:305px;width:90px;height:20px;background:var(--accent-soft);border-radius:3px}
.badge{left:160px;top:310px;width:80px;height:80px;border-radius:50%;background:var(--paper);border:2px solid var(--accent);display:flex;align-items:center;justify-content:center;text-align:center;font-size:8px;line-height:1.5;color:var(--ink)}
.advice-title{left:14px;top:392px;font-size:11px;font-weight:600}
.contact-opt{top:420px;width:100px}
.contact-opt .label{display:flex;align-items:center;gap:5px;color:var(--accent);font-size:7.4px;margin-bottom:8px}
.opt-divider{left:118px;top:418px;width:1px;height:48px;background:var(--accent-soft)}
.address{left:14px;top:482px;width:205px;font-size:7.2px;line-height:1.55}

/* cover */
.brand{left:0;top:20px;width:230px;text-align:center}
.brand-mark{display:block;margin:0 auto 6px;width:30px;height:30px;border-radius:50%;background:var(--accent)}
.brand-name{font-size:15px;font-weight:700;color:var(--ink)}
.brand-sub{font-size:6.5px;letter-spacing:1.6px;font-weight:700;margin-top:3px}
.pets{left:10px;top:110px;width:210px;height:140px;background:linear-gradient(90deg,#8f8579,#b3835a 60%,#c49468);border-radius:40px 40px 0 0}
.cover-box{left:14px;top:235px;width:202px;height:270px;background:linear-gradient(180deg,var(--accent-deep),#c49570);color:var(--on-accent);text-align:center;padding:30px 14px 0}
.cover-title{font-size:12px;line-height:1.3;font-weight:600}
.cover-rule{width:40px;height:1px;background:var(--on-accent);margin:14px auto 16px;opacity:.8}
.cover-text{font-size:7.4px;line-height:1.5}
.cover-tagline{margin-top:16px;font-size:11px;font-weight:700}

/* inside left */
.scene-photo{left:14px;top:14px;width:202px;height:150px;background:linear-gradient(180deg,#7f9fc2 0%,#a9b8c2 40%,#c48f5c 62%,#9b8c7c 100%)}
.focus-title{left:14px;top:178px;font-size:11px;font-weight:600}
.focus-text{left:14px;top:198px;width:196px;font-size:7.2px;line-height:1.5}
.services{left:14px;top:330px;width:202px;height:176px;background:var(--accent-deep);color:var(--on-accent);padding:14px 12px}
.services h2,.tcm h2{font-size:11px;font-weight:600;margin-bottom:10px}
.ticks{list-style:none}
.ticks li{display:flex;align-items:center;gap:4px;font-size:7.6px;line-height:1}
.services .ticks li{margin-bottom:7px}

/* inside right */
.tcm{left:14px;top:14px;width:202px;height:150px;background:var(--accent);color:var(--on-accent);padding:22px 12px}
.tcm p{font-size:7px;line-height:1.55}
.uses-title{left:18px;top:180px;font-size:7.6px;font-weight:700}
.uses{left:18px;top:198px;width:200px}
.uses li{margin-bottom:7px;color:var(--ink-soft)}
.food-photo{left:14px;top:320px;width:96px;height:186px;background:linear-gradient(160deg,#6b4f3a,#b87a4d 55%,#d3a37a)}
.acu-photo{left:116px;top:320px;width:100px;height:186px;background:linear-gradient(160deg,#8d8f94,#c7b39c)}
</style>
</head>
<body>

<section class="spread spread--outside">
  <article class="panel panel--white">
    <div class="abs about-box"></div>
    <div class="photo portrait" role="img" aria-label="Porträtfoto der Therapeutin mit einer weißen Katze im Arm"></div>
    <h2 class="abs about-title" style="color:var(--on-accent)">Über mich</h2>
    <p class="abs about-text t-small" style="color:var(--on-accent)">Mit meiner langjährigen Erfahrung, fundierter Expertise und viel Geduld stehe ich dir und deinem Tier zur Seite. <span class="strong">Moderne Trainingsmethoden und aktuelle wissenschaftliche Erkenntnisse</span> helfen mir, das Zusammenleben von Mensch und Tier jeden Tag zu verbessern.</p>
    <p class="abs about-invite t-small" style="color:var(--on-accent)">Lass uns gemeinsam die Welt deiner Haustiere bereichern!</p>
    <div class="abs signature" role="img" aria-label="Handschriftliche Unterschrift Marlene Hovers"></div>
    <div class="abs badge"><span><span class="strong">Kostenlose</span><br>Erstberatung!</span></div>
    <h3 class="abs advice-title">Lassen Sie sich beraten!</h3>
    <div class="abs contact-opt" style="left:14px">
      <div class="label">
        <svg width="14" height="10" viewBox="0 0 14 10"><rect x="1" y="1" width="12" height="7" fill="none" stroke="currentColor"/><line x1="4" y1="9.5" x2="10" y2="9.5" stroke="currentColor"/></svg>Online</div>
      <p class="t-small">Entspannt von zuhause<br>per Videokonferenz</p>
    </div>
    <div class="abs opt-divider"></div>
    <div class="abs contact-opt" style="left:126px">
      <div class="label">
        <svg width="12" height="12" viewBox="0 0 12 12"><path d="M1 6 L6 1 L11 6 V11 H1 Z" fill="none" stroke="currentColor"/><rect x="5" y="7" width="2" height="4" fill="none" stroke="currentColor"/></svg>Hausbesuche</div>
      <p class="t-small">Im Raum Karlsruhe auch<br>vor Ort</p>
    </div>
    <p class="abs address">Marlene Hovers · Birkenweg 14 · 76131 Karlsruhe<br>Tel. 0176 / 0000 4821 · info@pfotenruh-praxis.de<br><span class="strong">www.pfotenruh-praxis.de</span></p>
  </article>

  <article class="panel panel--grey">
    <div class="abs brand">
      <span class="brand-mark"></span>
      <div class="brand-name">Pfotenruh</div>
      <div class="brand-sub">MARLENE HOVERS</div>
    </div>
    <div class="photo pets" role="img" aria-label="Katze und Hund schauen über den Rand der Box"></div>
    <div class="abs cover-box">
      <h1 class="cover-title">Tiertherapeutin für TCVM und Ernährungsberaterin für Hunde und Katzen</h1>
      <div class="cover-rule"></div>
      <p class="cover-text">Mittels <span class="strong">Akupunktur, Lasertherapie, Mykotherapie</span> und <span class="strong">Ernährungsberatung</span> kommt es zu einer Linderung vorhandener Schmerzen, eine verbesserte Regulation der Organe und einer Steigerung das Wohlbefindens sowie Lebensqualität.</p>
      <p class="cover-tagline">Dein Tier im Fokus!</p>
    </div>
  </article>
</section>

<section class="spread spread--inside">
  <article class="panel panel--grey" style="background:#eeeeee">
    <div class="photo scene-photo" role="img" aria-label="Katze und Hund liegen nebeneinander auf einem sonnigen Hof"></div>
    <h2 class="abs focus-title">Dein Tier im Fokus</h2>
    <p class="abs focus-text">Mein Ziel ist es, das innere Gleichgewicht deines Tieres wiederherzustellen und die Selbstheilungskräfte zu aktivieren, um ein schmerzfreies und gesundes Leben zu ermöglichen.<br>Meine mobilen Therapiemethoden lindern nicht nur Symptome, sondern bekämpfen auch die Ursachen. So kann sich dein Tier in vertrauter Umgebung entspannen.</p>
    <div class="abs services">
      <h2>Meine Dienstleistungen</h2>
      <ul class="ticks">
        <li><svg width="8" height="8" viewBox="0 0 8 8"><path d="M1 4 L3 6.5 L7 1" fill="none" stroke="currentColor" stroke-width="1.1"/></svg>Katzenverhaltenstraining</li>
        <li><svg width="8" height="8" viewBox="0 0 8 8"><path d="M1 4 L3 6.5 L7 1" fill="none" stroke="currentColor" stroke-width="1.1"/></svg>Ernährungsberatung für Hunde &amp; Katzen</li>
        <li><svg width="8" height="8" viewBox="0 0 8 8"><path d="M1 4 L3 6.5 L7 1" fill="none" stroke="currentColor" stroke-width="1.1"/></svg>Ganzheitliche Behandlung nach TCVM</li>
        <li><svg width="8" height="8" viewBox="0 0 8 8"><path d="M1 4 L3 6.5 L7 1" fill="none" stroke="currentColor" stroke-width="1.1"/></svg>Akupunktur</li>
        <li><svg width="8" height="8" viewBox="0 0 8 8"><path d="M1 4 L3 6.5 L7 1" fill="none" stroke="currentColor" stroke-width="1.1"/></svg>Laserbehandlung</li>
        <li><svg width="8" height="8" viewBox="0 0 8 8"><path d="M1 4 L3 6.5 L7 1" fill="none" stroke="currentColor" stroke-width="1.1"/></svg>Chinesische Kräuterheilkunde</li>
        <li><svg width="8" height="8" viewBox="0 0 8 8"><path d="M1 4 L3 6.5 L7 1" fill="none" stroke="currentColor" stroke-width="1.1"/></svg>Mykotherapie</li>
        <li><svg width="8" height="8" viewBox="0 0 8 8"><path d="M1 4 L3 6.5 L7 1" fill="none" stroke="currentColor" stroke-width="1.1"/></svg>Darmaufbau</li>
      </ul>
    </div>
  </article>

  <article class="panel panel--white">
    <div class="abs tcm">
      <h2>Was ist TCM?</h2>
      <p>Die traditionelle chinesische Veterinärmedizin (TCVM) ist ein ganzheitliches System, das durch Akupunktur, Kräuterheilkunde und andere Methoden das Qi, die Lebensenergie, ins Gleichgewicht bringt und die Selbstheilungskräfte aktiviert. Sie diagnostiziert detailliert, um energetische Disharmonien zu erkennen und zu beheben.</p>
    </div>
    <h3 class="abs uses-title">Vielfältige Einsatzgebiete der TCM</h3>
    <ul class="abs ticks uses">
      <li><svg width="8" height="8" viewBox="0 0 8 8"><path d="M1 4 L3 6.5 L7 1" fill="none" stroke="var(--accent)" stroke-width="1.1"/></svg>Schmerzen &amp; Gelenkserkrankungen</li>
      <li><svg width="8" height="8" viewBox="0 0 8 8"><path d="M1 4 L3 6.5 L7 1" fill="none" stroke="var(--accent)" stroke-width="1.1"/></svg>Lähmungen &amp; Nervenverletzungen</li>
      <li><svg width="8" height="8" viewBox="0 0 8 8"><path d="M1 4 L3 6.5 L7 1" fill="none" stroke="var(--accent)" stroke-width="1.1"/></svg>Atemwegs- &amp; Entzündungserkrankungen</li>
      <li><svg width="8" height="8" viewBox="0 0 8 8"><path d="M1 4 L3 6.5 L7 1" fill="none" stroke="var(--accent)" stroke-width="1.1"/></svg>Immunschwäche &amp; Allergien</li>
      <li><svg width="8" height="8" viewBox="0 0 8 8"><path d="M1 4 L3 6.5 L7 1" fill="none" stroke="var(--accent)" stroke-width="1.1"/></svg>Epilepsie &amp; hormonelle Störungen</li>
      <li><svg width="8" height="8" viewBox="0 0 8 8"><path d="M1 4 L3 6.5 L7 1" fill="none" stroke="var(--accent)" stroke-width="1.1"/></svg>Wundheilung &amp; Narbenbehandlung</li>
      <li><svg width="8" height="8" viewBox="0 0 8 8"><path d="M1 4 L3 6.5 L7 1" fill="none" stroke="var(--accent)" stroke-width="1.1"/></svg>Stress, Angst, Altersbeschwerden</li>
    </ul>
    <div class="photo food-photo" role="img" aria-label="Schale mit frischem Tierfutter, Gemüse und Hundekeksen"></div>
    <div class="photo acu-photo" role="img" aria-label="Akupunkturnadeln im Fell eines Hundes"></div>
  </article>
</section>

</body>
</html>
```